Harbourline construction company Business card design

I need a business card design for my company. I have a logo but dont have business cards with our logo..

www.harbourlineconstructco.com.au

The logo is on the website

I need the same details as this design I have attached. we have changed the logo and colours. just like the website

Industry/Entity Type

Building

```html
<!DOCTYPE html>
<html lang="en">
<head>
<meta charset="utf-8">
<title>Harbourline Construction Company – Business Card</title>
<link href="https://fonts.googleapis.com/css2?family=Cinzel:wght@600&family=Open+Sans:wght@400;600&display=swap" rel="stylesheet">
<style>
  :root {
    --backdrop: #2b2d30;
    --brand-blue: #1089c3;
    --brand-blue-deep: #0a78b0;
    --card-white: #ffffff;
    --card-mist: #e7e8ea;
    --band-grey: #b9bbbf;
    --ink: #1d1d1f;
    --ink-soft: #3b3c40;
    --rule: #2a2a2c;
  }
  * { box-sizing: border-box; margin: 0; padding: 0; }
  html, body { width: 1200px; height: 900px; overflow: hidden; }
  body {
    background: var(--backdrop);
    display: flex;
    flex-direction: column;
    align-items: center;
    justify-content: center;
    gap: 40px;
    font-family: "Open Sans", Arial, sans-serif;
  }
  .card {
    position: relative;
    width: 700px;
    height: 400px;
    border-radius: 26px;
    overflow: hidden;
    box-shadow: 0 10px 24px rgba(0,0,0,.45);
  }

  /* ---------- front ---------- */
  .card--front {
    background: linear-gradient(to bottom, var(--card-white) 0 31%, var(--brand-blue) 31% 100%);
  }
  .front-brand {
    position: absolute;
    left: 0; right: 0; top: 74px;
    display: flex; flex-direction: column; align-items: center;
    color: var(--card-white);
  }
  .front-brand .brand-square {
    width: 44px; height: 44px;
    background: var(--brand-blue);
    border: 3px solid var(--card-white);
    margin-bottom: 22px;
  }
  .front-brand .brand-name {
    font-family: "Cinzel", Georgia, serif;
    font-weight: 600;
    font-size: 30px;
    letter-spacing: 2px;
    text-align: center;
    line-height: 1.15;
  }
  .front-rule {
    position: absolute;
    top: 232px; left: 40px; right: 40px;
    display: flex; align-items: center; gap: 16px;
  }
  .front-rule .line { flex: 1; height: 1px; background: rgba(255,255,255,.75); }
  .front-rule .tagline {
    font-size: 12.5px; font-weight: 600; color: var(--card-white);
    text-align: center; line-height: 1.35;
  }

  /* ---------- back ---------- */
  .card--back {
    background: linear-gradient(135deg, var(--card-white) 0%, var(--card-white) 45%, var(--card-mist) 100%);
  }
  .band-grey {
    position: absolute; left: 0; bottom: 0;
    width: 430px; height: 46px;
    background: linear-gradient(to bottom, #cfd0d3, var(--band-grey));
    clip-path: polygon(0 0, 100% 0, 92% 100%, 0 100%);
  }
  .band-blue {
    position: absolute; right: 0; bottom: 0;
    width: 340px; height: 82px;
    background: linear-gradient(to bottom, var(--brand-blue), var(--brand-blue-deep));
    clip-path: polygon(18% 0, 100% 0, 100% 100%, 0 100%);
  }
  .reg-number {
    position: absolute; right: 36px; bottom: 52px;
    font-size: 15px; color: rgba(255,255,255,.8);
  }
  .back-brand {
    position: absolute; left: 36px; top: 70px; width: 300px;
    display: flex; flex-direction: column; align-items: center;
  }
  .back-brand .brand-square {
    width: 54px; height: 54px; background: var(--brand-blue);
    margin-bottom: 24px;
  }
  .back-brand .brand-name {
    font-family: "Cinzel", Georgia, serif;
    font-weight: 600; font-size: 27px; letter-spacing: 1.5px;
    color: var(--brand-blue); text-align: center; line-height: 1.15;
    padding-bottom: 10px; border-bottom: 1px solid var(--rule);
  }
  .back-brand .tagline {
    margin-top: 6px; font-size: 12.5px; font-weight: 600;
    color: var(--ink-soft); text-align: center; line-height: 1.35;
  }
  .divider {
    position: absolute; left: 360px; top: 54px;
    width: 1px; height: 210px; background: var(--rule);
  }
  .contact {
    position: absolute; left: 392px; top: 62px;
  }
  .contact .person {
    font-family: "Cinzel", Georgia, serif; font-weight: 600;
    font-size: 24px; color: var(--ink); letter-spacing: 1px;
  }
  .contact .role {
    font-size: 14px; color: var(--brand-blue);
    text-align: right; margin-top: -4px; width: 212px;
  }
  .contact ul { list-style: none; margin-top: 22px; }
  .contact li {
    display: flex; align-items: center; gap: 12px;
    font-size: 15px; color: var(--ink); margin-bottom: 6px;
  }
  .contact svg { width: 16px; height: 16px; fill: var(--brand-blue); flex: none; }
</style>
</head>
<body>

<section class="card card--front" aria-label="Card front">
  <div class="front-brand">
    <span class="brand-square"></span>
    <p class="brand-name">Harbourline<br>Construction Company</p>
  </div>
  <div class="front-rule">
    <span class="line"></span>
    <p class="tagline">New Homes • Additions &amp; Renovations<br>Domestic &amp; Commercial Builders</p>
    <span class="line"></span>
  </div>
</section>

<section class="card card--back" aria-label="Card back">
  <div class="band-grey"></div>
  <div class="band-blue"></div>
  <p class="reg-number">Reg. No. 20815</p>

  <div class="back-brand">
    <span class="brand-square"></span>
    <p class="brand-name">Harbourline<br>Construction Company</p>
    <p class="tagline">New Homes • Additions &amp; Renovations<br>Domestic &amp; Commercial Builders</p>
  </div>

  <div class="divider"></div>

  <div class="contact">
    <p class="person">Marek Dalton</p>
    <p class="role">director</p>
    <ul>
      <li>
        <svg viewBox="0 0 16 16" aria-label="Phone"><circle cx="8" cy="8" r="7.5" fill="none" stroke="#1089c3" stroke-width="1.2"/><path d="M5.5 4.2l1.3-.3.8 2-1 .7c.4 1 1.1 1.8 2.1 2.3l.7-1 2 .8-.3 1.3c-3 .4-6-2.6-5.6-5.8z"/></svg>
        08 9400 1180
      </li>
      <li>
        <svg viewBox="0 0 16 16" aria-label="Mobile"><path d="M4.5 1h7a1 1 0 0 1 1 1v12a1 1 0 0 1-1 1h-7a1 1 0 0 1-1-1V2a1 1 0 0 1 1-1zm.8 2v8.5h5.4V3zM8 12.3a.9.9 0 1 0 0 1.8.9.9 0 0 0 0-1.8z"/></svg>
        08 9400 1180
      </li>
      <li>
        <svg viewBox="0 0 16 16" aria-label="Fax"><path d="M4 1h6l2 2v3H4zM2 7h12a1 1 0 0 1 1 1v5H1V8a1 1 0 0 1 1-1zm2 5h8v3H4z"/></svg>
        0412 550 316
      </li>
      <li>
        <svg viewBox="0 0 16 16" aria-label="Email"><path d="M1 3h14v1.2L8 9 1 4.2zm0 2.6l7 4.8 7-4.8V13H1z"/></svg>
        harbourlineco@mailbox.com
      </li>
    </ul>
  </div>
</section>

</body>
</html>
```